Design for Training Manuals

We need a graphic design for new training manuals for our organization called Lanternfield Trust, Inc. We are a children's rights NGO based in the Philippines. We are running an advocacy campaign called Raise Every Hand which advocates for the prevention of child sexual abuse and sexual exploitation of children. The Raise Every Hand Campaign is gaining momentum in various countries around the world and we would like to provide our constituents with inspiring training materials that will enable them to carry out the work of protecting children's rights.
Because of the sensitive nature of the subject matter, we would like to present a non-threatening light design, with a creative edge, that incorporates our Raise Every Hand logo. Also, I have attached an image from which you can design from.
Please feel free to visit our website for inspiration: www.lanternfieldtrust.org
Updates
Dear Designers,
I am excited about this project. I have uploaded a couple of our training modules. Overall there are 2 levels: Level 1 with 3 training modules and Level 2 also with 3 training modules.
Thank you,
Teresa
Target Market(s)
Non-government workers, government workers, teachers, social workers...
Industry/Entity Type
Graphic Design
Look and feel
Each slider illustrates characteristics of the customer's brand and the style your logo design should communicate.

```html
<!DOCTYPE html>
<html lang="en">
<head>
<meta charset="utf-8">
<title>Raise Every Hand — Training manual: module 1</title>
<link href="https://fonts.googleapis.com/css2?family=Arimo:wght@400;700&display=swap" rel="stylesheet">
<style>
  :root {
    --paper: #ffffff;
    --ink: #111111;
    --steel: #6a6d72;
    --violet: #3b2a8f;
    --orange: #f07828;
    --sun: #f5a623;
    --crowd-warm: #e8a25a;
    --crowd-red: #d8483c;
    --crowd-blue: #5a86c4;
    --crowd-dark: #3a3030;
    --crowd-light: #f3e6cf;
  }
  * { margin: 0; padding: 0; box-sizing: border-box; }
  html, body { width: 845px; height: 1200px; overflow: hidden; background: var(--paper); }
  .cover {
    position: relative;
    width: 845px;
    height: 1200px;
    background: var(--paper);
    font-family: "Arimo", Arial, sans-serif;
    color: var(--ink);
  }
  .org-mark {
    position: absolute;
    left: 92px;
    top: 90px;
    display: flex;
    flex-direction: column;
    align-items: center;
    width: 126px;
  }
  .org-mark__dot {
    width: 68px;
    height: 68px;
    border-radius: 50%;
    background: var(--sun);
  }
  .org-mark__name {
    margin-top: 10px;
    font-size: 10px;
    font-weight: 700;
    letter-spacing: 0.2px;
    color: var(--ink);
    white-space: nowrap;
  }
  .campaign-name {
    position: absolute;
    left: 92px;
    top: 190px;
    font-size: 70px;
    font-weight: 400;
    letter-spacing: -1px;
    color: var(--steel);
    white-space: nowrap;
  }
  .tagline {
    position: absolute;
    left: 256px;
    top: 315px;
    font-size: 19px;
    font-weight: 700;
    color: var(--ink);
    white-space: nowrap;
  }
  .module-title {
    position: absolute;
    left: 300px;
    top: 385px;
    font-size: 40px;
    font-weight: 400;
    color: var(--violet);
    white-space: nowrap;
  }
  .module-title__number { color: var(--orange); }
  .crowd-art {
    position: absolute;
    left: 0;
    top: 560px;
    width: 845px;
    height: 640px;
  }
</style>
</head>
<body>
  <main class="cover">
    <div class="org-mark">
      <span class="org-mark__dot"></span>
      <span class="org-mark__name">LANTERNFIELD TRUST, INC.</span>
    </div>

    <h1 class="campaign-name">Raise Every Hand</h1>
    <p class="tagline">Stop child sexual abuse and exploitation</p>
    <h2 class="module-title">Training manual: <span class="module-title__number">module 1</span></h2>

    <svg class="crowd-art" viewBox="0 0 845 640" role="img"
         aria-label="Colourful hand-drawn illustration of a crowd of children and adults seen from behind, holding signs about children's rights">
      <defs>
        <linearGradient id="crowdTones" x1="0" y1="0" x2="1" y2="1">
          <stop offset="0" stop-color="var(--crowd-red)"/>
          <stop offset="0.25" stop-color="var(--crowd-warm)"/>
          <stop offset="0.5" stop-color="var(--crowd-light)"/>
          <stop offset="0.75" stop-color="var(--crowd-blue)"/>
          <stop offset="1" stop-color="var(--crowd-dark)"/>
        </linearGradient>
      </defs>
      <path fill="url(#crowdTones)" d="M0 110 C40 60 90 50 130 70 C170 40 210 10 260 30 C300 50 330 60 360 70 C400 40 440 20 480 60 C520 40 560 30 600 70 C650 30 700 10 750 40 C790 60 820 90 845 120 L845 640 L0 640 Z"/>
    </svg>
  </main>
</body>
</html>
```